New Business Card/Website Logo

We need a business card design for a new company based in Sydney. The company focuses mainly in construction in the field of form work and concreting. Attached is the logo being used already which can be used as a base for a new design, the current one is simply too bland and we are looking to spruce it up so it stands out and looks nicer. The logo would also be used on the website which is currently under construction. The attached image has the name, mobile and also the license number which needs to be there. The current email address on there can be removed and can be replaced with the website http://www.pillarvane.com.au, thanks!
Updates

Target Market(s)

Construction industry. Focusing on form work and concreting

Industry/Entity Type

Construction

Requirements
Must have
• License # on card along with website http://www.pillarvane.com.au and mobile phone number
Nice to have
• You have freedom with the design. The current design was a mock up done quite quickly. Please just keep in mind the target audience - construction, thanks.
Should not have
• the breezepost email address can be removed(refer picture) and replaced somewhere on the design with the website http://www.pillarvane.com.au

```html
<!DOCTYPE html>
<html lang="en">
<head>
<meta charset="utf-8">
<title>Pillarvane – Business Card</title>
<link href="https://fonts.googleapis.com/css2?family=Josefin+Sans:wght@400;600&family=Tinos&display=swap" rel="stylesheet">
<style>
  :root {
    --brand-green: #3f9e3c;
    --brand-green-dark: #2f7d2d;
    --paper: #f7f6f2;
    --ink: #2b2b2b;
    --muted: #6b6b66;
    --backdrop: #e4e2dd;
    --on-green: #ffffff;
  }
  * { margin: 0; padding: 0; box-sizing: border-box; }
  html, body {
    width: 1200px; height: 800px; overflow: hidden;
    background: var(--backdrop);
  }
  .card {
    position: absolute; left: 75px; top: 100px;
    width: 1050px; height: 600px; overflow: hidden;
    background: var(--paper);
    box-shadow: 0 6px 24px rgba(0,0,0,0.12);
    font-family: "Tinos", "Times New Roman", serif;
    color: var(--ink);
  }
  .edge-band {
    position: absolute; left: 0; top: 0; bottom: 0; width: 22px;
    background: var(--brand-green);
  }
  .base-band {
    position: absolute; left: 0; right: 0; bottom: 0; height: 14px;
    background: var(--brand-green-dark);
  }
  .brand {
    position: absolute; right: 90px; top: 90px;
    display: flex; align-items: center; gap: 16px;
  }
  .brand-square { width: 40px; height: 40px; background: var(--brand-green); }
  .brand-name {
    font-family: "Josefin Sans", "Futura", sans-serif;
    font-weight: 600; font-size: 40px; letter-spacing: 4px;
    color: var(--brand-green); line-height: 1; padding-top: 6px;
  }
  .licence {
    position: absolute; right: 90px; top: 152px;
    font-size: 22px; color: var(--ink);
  }
  .rule {
    position: absolute; left: 90px; right: 90px; top: 290px;
    height: 2px; background: var(--brand-green); opacity: 0.35;
  }
  .person { position: absolute; left: 90px; top: 340px; }
  .person-name {
    display: inline-block;
    background: var(--brand-green); color: var(--on-green);
    font-family: "Josefin Sans", "Futura", sans-serif;
    font-weight: 400; font-size: 30px; letter-spacing: 1px;
    padding: 8px 16px 4px; border-radius: 6px;
  }
  .person-role { margin-top: 14px; padding-left: 16px; font-size: 22px; color: var(--muted); }
  .contacts {
    position: absolute; left: 106px; top: 462px;
    list-style: none; display: flex; flex-direction: column; gap: 18px;
  }
  .contact { display: flex; align-items: center; gap: 14px; font-size: 22px; }
  .contact-icon { width: 26px; height: 26px; flex: none; }
  .accent { color: var(--brand-green); }
</style>
</head>
<body>
  <main class="card">
    <span class="edge-band"></span>
    <span class="base-band"></span>

    <div class="brand">
      <span class="brand-square"></span>
      <span class="brand-name">PILLARVANE</span>
    </div>
    <p class="licence">Licence: 384912B</p>

    <span class="rule"></span>

    <section class="person">
      <h1 class="person-name">Mateo Ferreira</h1>
      <p class="person-role">Founder &amp; CEO</p>
    </section>

    <ul class="contacts">
      <li class="contact">
        <svg class="contact-icon" viewBox="0 0 26 26" aria-hidden="true">
          <circle cx="13" cy="13" r="13" fill="var(--brand-green)"/>
          <path d="M9 7c1 0 2 2.5 2 3s-1 1-1 1.6c.6 1.8 2.4 3.6 4.2 4.2.6 0 1-1 1.6-1s3 1 3 2-1.5 2.2-2.5 2.2C11 19 7 15 7 9c0-1 1-2 2-2z" fill="var(--on-green)"/>
        </svg>
        <span>0412 555 019</span>
      </li>
      <li class="contact">
        <svg class="contact-icon" viewBox="0 0 26 26" aria-hidden="true">
          <circle cx="13" cy="13" r="13" fill="var(--brand-green)"/>
          <circle cx="13" cy="13" r="6.5" fill="none" stroke="var(--on-green)" stroke-width="1.4"/>
          <ellipse cx="13" cy="13" rx="2.8" ry="6.5" fill="none" stroke="var(--on-green)" stroke-width="1.2"/>
          <path d="M6.5 13h13" stroke="var(--on-green)" stroke-width="1.2"/>
        </svg>
        <span>http://www.<span class="accent">pillarvane</span>.com.au</span>
      </li>
    </ul>
  </main>
</body>
</html>
```